Australian Careers Business Needs 2 Banner Ad Design

We need a banner ad design for a new company based in Australia called Bright Sparrows. We provide career tools and insights to young professionals. Our target market is 20-30 year olds.

We would like to see designs that attract users on the site to click on the banner and sign up for a weekly newsletter. The newsletter will feature a blog, cheat sheets etc. Inspiration in their inbox!

The second banner is to attract users to sign up for a Horizon Gathering. They would click on it to find out more information and then register with their email address. This convention is a 1 day workshop designed to enhance young professionals abilities to give their best at work. There will CEO insights etc.

Use of images or flash is ok. Needs to look very professional and presented in accordance to the current colour scheme in place. Visit http://www.brightsparrows-demo.com/home to understand.

Banner sizes 300 x 250.
Mandatory use of Corporate Colours required on Font.
R66 G73 B74
R242 G240 B230
R38 G128 B138

No logo necessary.

Hi All,As both banners will feature on the Bright Sparrows site there is no need for a logo or hyperlink to the site.I would like to see some better images, and a bit more creative flair.Please don't use single female images as I am wanting to avoid the women in business perception. We cater to young professionals.Some suggestions for lines to utilise on the newsletter ad:Click here for weekly career tipsInvest in your career for free hereJoin the weekly conversationWeekly career tips in your inboxSign up for our weekly newsletterSome suggestions for lines to use on the horizon gathering ad:Register for the Horizon Gathering - Find out how to get ahead of your peersAre you a millennial climbing the corporate ladder? Find out how to rise to the topInterested in hearing from experts who recognise millennials are our future business leaders? Click here.Thanks,Megan Added Friday, April 3, 2015

Target Market(s)

20-30 years

Industry/Entity Type

Business

Font styles to use
Sans Serif

Requirements
Must have
• Please use images in the attached as options
Should not have
• NO LOGO - Its already onsite so not needed.

```html
<!DOCTYPE html>
<html lang="en">
<head>
<meta charset="utf-8">
<title>Bright Sparrows Banner Set</title>
<link href="https://fonts.googleapis.com/css2?family=Montserrat:wght@600;700&family=Questrial&family=Arimo:wght@400&display=swap" rel="stylesheet">
<style>
:root{
  --teal:#26808a;
  --teal-deep:#1f5f66;
  --slate:#42494a;
  --cream:#f2f0e6;
  --white:#ffffff;
  --photo-teal:linear-gradient(135deg,#3f8e93 0%,#2b6f75 55%,#1f5a60 100%);
  --photo-room:linear-gradient(180deg,#e4e2dc 0%,#cfcdc7 55%,#8d9093 100%);
  --photo-office:linear-gradient(120deg,#f0f0ee 0%,#d9d8d4 50%,#6f7173 100%);
}
*{box-sizing:border-box;margin:0;padding:0}
html,body{width:1200px;height:700px;overflow:hidden;background:var(--white)}
body{position:relative;font-family:'Montserrat',sans-serif}
.banner{position:absolute;width:300px;height:250px;overflow:hidden;box-shadow:0 10px 10px -6px rgba(0,0,0,.22)}
.photo{position:absolute}
.photo.teal{background:var(--photo-teal)}
.photo.room{background:var(--photo-room)}
.photo.office{background:var(--photo-office)}
.headline{position:absolute;left:0;width:100%;text-align:center;color:var(--cream);font-weight:700;line-height:1}
.band-cream{position:absolute;left:0;width:100%;background:var(--cream)}
.sub-cta{position:absolute;left:0;width:100%;text-align:center;color:var(--teal-deep);font-weight:700;font-size:18px;line-height:25px}
.email-field{position:absolute;display:flex;align-items:center;font-family:'Arimo',sans-serif;font-size:18px}
.email-field .box{display:inline-block;width:13px;height:13px;background:var(--cream);border:1px solid #999;margin-right:8px}
.screen{position:absolute;background:var(--teal);border:3px solid #2a2f30;display:flex;flex-direction:column;justify-content:center;align-items:center;text-align:center;color:var(--cream);font-weight:700}
.btn{position:absolute;background:var(--teal);color:var(--white);font-family:'Questrial',sans-serif;display:flex;align-items:center;justify-content:center;border-radius:4px}
.cursor{position:absolute;width:22px;height:26px}
.footer-band{position:absolute;left:0;top:622px;width:1200px;height:78px;background:var(--teal);border-top:4px solid #3a3f40;color:var(--white);font-family:'Questrial',sans-serif;font-size:41px;line-height:72px;padding-left:44px;letter-spacing:.5px}
</style>
</head>
<body>

<svg width="0" height="0" style="position:absolute">
  <symbol id="hand" viewBox="0 0 22 26">
    <path d="M7 2c1.2 0 2 .8 2 2v8l1-.2V9.5c0-1 2.6-1 2.6 0V12l.9-.1v-1.3c0-1 2.6-1 2.6 0v1.6l.9-.1c0-1 2.5-1 2.5 0v6.5c0 3.5-2.4 6.4-6 6.4h-2.5c-2 0-3.4-1-4.4-2.6L2.2 16c-.6-1 .8-2.4 2-1.4L5 15.4V4c0-1.2.8-2 2-2z" fill="#fff" stroke="#222" stroke-width="1.2"/>
  </symbol>
  <symbol id="envelope" viewBox="0 0 24 16">
    <rect x="1" y="1" width="22" height="14" fill="#fff" stroke="#fff"/>
    <path d="M1 1l11 8 11-8" fill="none" stroke="#26808a" stroke-width="1.5"/>
  </symbol>
</svg>

<!-- Newsletter banner: headline with email field -->
<section class="banner" style="left:45px;top:35px">
  <div class="photo teal" role="img" aria-label="Hand holding a smartphone showing a news page" style="left:0;top:0;width:300px;height:180px"></div>
  <div class="headline" style="top:14px;font-size:40px">WEEKLY</div>
  <div class="headline" style="top:59px;font-size:29px">CAREER</div>
  <div class="headline" style="top:94px;font-size:23px">TIPS IN YOUR INBOX</div>
  <div class="email-field" style="left:7px;top:135px;width:288px;height:32px;background:var(--teal-deep);border-radius:16px;padding-left:24px;color:var(--cream);box-shadow:inset 0 0 0 2px #17474c">
    <span class="box"></span>yourname@email.here
  </div>
  <div class="band-cream" style="top:180px;height:70px"></div>
  <div class="sub-cta" style="top:189px">SIGN UP FOR OUR<br>WEEKLY NEWSLETTE</div>
</section>

<!-- Newsletter banner: click here panel -->
<section class="banner" style="left:468px;top:35px">
  <div style="position:absolute;left:0;top:0;width:133px;height:250px;background:var(--teal)"></div>
  <div class="photo office" role="img" aria-label="Two young professionals looking at a phone in an office" style="left:133px;top:0;width:167px;height:250px"></div>
  <div style="position:absolute;left:9px;top:22px;width:115px;height:33px;background:var(--cream);border-radius:17px;color:var(--teal);font-weight:700;font-size:15px;display:flex;align-items:center;justify-content:center">CLICK HERE</div>
  <svg class="cursor" style="left:97px;top:48px"><use href="#hand"/></svg>
  <div style="position:absolute;left:0;top:72px;width:133px;text-align:center;color:var(--cream);font-weight:700;font-size:29px;line-height:35px">FOR<br>WEEKLY<br>CAREER<br>TIPS</div>
</section>

<!-- Gathering banner: subscribe -->
<section class="banner" style="left:859px;top:35px">
  <div class="photo room" role="img" aria-label="Speaker presenting to a seated audience in a conference room" style="left:0;top:0;width:300px;height:250px"></div>
  <div class="screen" style="left:70px;top:14px;width:222px;height:102px;font-size:26px;line-height:31px">HORIZON<br>GATHERING</div>
  <div style="position:absolute;left:0;top:153px;width:300px;height:50px;background:rgba(242,240,230,.85);text-align:center;color:var(--teal);font-weight:700;font-size:15px;line-height:20px;padding-top:5px">FIND OUT HOW TO GET AHEAD<br>OF YOUR PEERS</div>
  <div class="btn" style="left:61px;top:215px;width:170px;height:25px;font-size:16px">subscribe now</div>
  <svg class="cursor" style="left:220px;top:220px"><use href="#hand"/></svg>
</section>

<!-- Newsletter banner: square field -->
<section class="banner" style="left:45px;top:340px">
  <div class="photo teal" role="img" aria-label="Hand holding a smartphone showing a news page" style="left:0;top:0;width:300px;height:186px"></div>
  <div class="headline" style="top:81px;font-size:23px">WEEKLY CAREER</div>
  <div class="headline" style="top:105px;font-size:11px">TIPS IN YOUR INBOX</div>
  <div class="band-cream" style="top:186px;height:64px"></div>
  <div style="position:absolute;left:9px;top:200px;width:38px;height:34px;background:var(--teal);display:flex;align-items:center;justify-content:center">
    <svg width="24" height="16"><use href="#envelope"/></svg>
  </div>
  <div class="email-field" style="left:54px;top:200px;width:239px;height:34px;border:1px solid #888;background:#f7f6f0;color:#666;justify-content:center">yourname@email.here</div>
</section>

<!-- Newsletter banner: pill field -->
<section class="banner" style="left:481px;top:340px">
  <div class="photo teal" role="img" aria-label="Hand holding a smartphone showing a news page" style="left:0;top:0;width:300px;height:186px"></div>
  <div class="headline" style="top:81px;font-size:23px">WEEKLY CAREER</div>
  <div class="headline" style="top:105px;font-size:11px">TIPS IN YOUR INBOX</div>
  <div class="band-cream" style="top:186px;height:64px"></div>
  <div class="email-field" style="left:6px;top:201px;width:288px;height:32px;border:3px solid #3a3f40;border-radius:16px;background:#e4e1d0;color:#555;padding-left:26px">
    <span class="box"></span>yourname@email.here
  </div>
</section>

<!-- Gathering banner: question -->
<section class="banner" style="left:859px;top:321px">
  <div class="photo room" role="img" aria-label="Speaker presenting to a seated audience in a conference room" style="left:0;top:0;width:300px;height:250px"></div>
  <div class="screen" style="left:70px;top:12px;width:222px;height:108px">
    <span style="font-size:16px;line-height:20px">ARE YOU</span>
    <span style="font-size:19px;line-height:24px">A MILLENNIAL</span>
    <span style="font-size:12px;line-height:14px">CLIMBING<br>THE CORPORATE LADDER?</span>
  </div>
  <div style="position:absolute;left:0;top:145px;width:300px;height:63px;background:rgba(38,128,138,.88);color:var(--white);font-family:'Arimo',sans-serif;font-size:13.5px;line-height:19px;text-align:center;padding-top:3px">Find out how to rise to the topInterested<br>in hearing from experts who recognise<br>millennials are our future business leaders?</div>
  <div class="btn" style="left:96px;top:215px;width:110px;height:28px;font-size:20px">click</div>
  <svg class="cursor" style="left:192px;top:220px"><use href="#hand"/></svg>
</section>

<footer class="footer-band">fully layered psd files, optimized jpeg, png and&nbsp; flash</footer>

</body>
</html>
```